Letterhead

We need a professional, compelling letterhead that can be used for print and email stationary. We have the logo and the letterhead styling and colors should blend seamlessly and be complimentary. Looking for something unique and thoughtful.
Updates

Reason: There are good ideas and am requesting changes to some ideas in order to make a final decision. Thank you for for submissions. Also, I have uploaded the ai file. Please use that file. Thank you.

If you cannot see the .ai version of the logo that I have tried to upload, please message me if you want to make changes to your submission or submit new design and I will send that file to you directly. This .ai will need to be used in order to ensure high quality printing. Thank you.

Target Market(s)

Clients. Business partners.

Industry/Entity Type

It Professional

Requirements
Must have
• Our logo incorporated. Also the phrase, or tag line - where business thrives.
Should not have
• Not boring. Not typical. Not too busy.

```html
<!DOCTYPE html>
<html lang="en">
<head>
<meta charset="utf-8">
<title>Meridian Advisory Group – Letterhead</title>
<link rel="stylesheet" href="https://fonts.googleapis.com/css2?family=Cormorant+Garamond:wght@600&display=swap">
<style>
  :root {
    --navy: #1d3a6b;
    --green: #2f9a45;
    --sheet: #fbfbfb;
    --sheet-top: #f1f1f1;
    --backdrop: #d9d9d9;
    --mark-faint: #ebebeb;
    --rule: #c4c9d1;
  }
  html, body {
    margin: 0;
    width: 1200px;
    height: 1000px;
    overflow: hidden;
    background: var(--backdrop);
  }
  .letterhead {
    position: absolute;
    left: 245px;
    top: 40px;
    width: 710px;
    height: 920px;
    background: linear-gradient(to bottom, var(--sheet-top), var(--sheet) 60%, #ffffff);
    box-shadow: 0 6px 18px rgba(0,0,0,0.25);
    overflow: hidden;
  }
  .edge-band {
    position: absolute;
    left: 0;
    top: 0;
    width: 8px;
    height: 100%;
    background: linear-gradient(to bottom, var(--navy), var(--green));
  }
  .edge-tab {
    position: absolute;
    left: 8px;
    top: 330px;
    width: 18px;
    height: 60px;
    background: var(--green);
  }
  .brand {
    position: absolute;
    right: 40px;
    top: 60px;
    display: flex;
    align-items: center;
    gap: 12px;
  }
  .brand-square {
    width: 18px;
    height: 18px;
    background: var(--green);
  }
  .brand-name {
    margin: 0;
    font-family: "Cormorant Garamond", Georgia, serif;
    font-weight: 600;
    font-size: 26px;
    line-height: 1;
    color: var(--navy);
    white-space: nowrap;
  }
  .brand-rule {
    position: absolute;
    right: 40px;
    top: 104px;
    width: 330px;
    height: 1px;
    background: var(--rule);
  }
  .watermark {
    position: absolute;
    left: 200px;
    top: 325px;
    width: 270px;
    height: 270px;
    border-radius: 50%;
    background: var(--mark-faint);
  }
</style>
</head>
<body>
  <main class="letterhead">
    <div class="edge-band"></div>
    <div class="edge-tab"></div>

    <header class="brand">
      <span class="brand-square"></span>
      <h1 class="brand-name">Meridian Advisory Group LLC</h1>
    </header>
    <div class="brand-rule"></div>

    <div class="watermark" role="img" aria-label="Faint large brand emblem placed behind the letter body"></div>
  </main>
</body>
</html>
```